BrackenfieldGoods.com

I need a site that I can sell dewatering equipment to the construction industry.
Ie, pipes fittings pumps and other such things needed to remove the groundwater on construction sites. Here in Florida, it’s needed almost everywhere seeing we are at sea level.
I want to be able to sell these products on the site and receive

Coding

Coded - Design and coding required

Number of Pages Required

1 page

```html
<!DOCTYPE html>
<html lang="en">
<head>
<meta charset="utf-8">
<title>Brackenfield Goods</title>
<link rel="stylesheet" href="https://fonts.googleapis.com/css2?family=Montserrat:wght@400;500;600;700&family=Roboto:wght@400;500&display=swap">
<style>
:root{
  --navy:#1f4a94;
  --navy-deep:#173c7e;
  --ink:#111;
  --white:#fff;
  --red:#e0202a;
  --grey:#666;
  --shadow:0 6px 18px rgba(0,0,0,.18);
}
*{margin:0;padding:0;box-sizing:border-box}
html,body{width:1200px;height:3734px;overflow:hidden;background:var(--white)}
body{font-family:'Roboto',sans-serif;color:var(--ink)}
.page{position:relative;width:1200px;height:3734px;overflow:hidden}
.abs{position:absolute}
.header{left:0;top:0;width:1200px;height:110px;background:var(--white);z-index:5}
.brand{left:100px;top:32px;font-family:'Montserrat',sans-serif;font-weight:700;font-size:30px;color:var(--navy)}
.nav{left:500px;top:66px;display:flex;gap:30px;font-family:'Montserrat',sans-serif;font-size:15px}
.nav a{color:var(--ink);text-decoration:none}
.nav a.active{color:var(--navy);font-weight:700}
.login{left:922px;top:20px;display:flex;align-items:center;gap:10px;font-family:'Montserrat',sans-serif;font-size:15px}
.search{left:930px;top:62px;width:180px;height:28px;border:1.5px solid var(--ink);border-radius:14px;font-size:12px;padding:6px 12px}
.hero{left:0;top:110px;width:1200px;height:620px;background:linear-gradient(90deg,#0c0f15 0%,#2b3038 45%,#8a9097 75%,#5a6068 100%)}
.hero-title{left:115px;top:250px;font-family:'Montserrat',sans-serif;font-weight:700;font-size:40px;line-height:52px;color:var(--white)}
.btn{display:inline-block;font-family:'Montserrat',sans-serif;font-size:15px;border-radius:24px;text-align:center}
.btn-navy{left:125px;top:395px;width:166px;height:46px;line-height:46px;background:var(--navy);color:var(--white);font-weight:600}
.btn-white{width:166px;height:46px;line-height:46px;background:var(--white);color:var(--navy)}
.blue-a{left:0;top:730px;width:1200px;height:770px;background:var(--navy)}
.tile{width:232px;height:232px;border-radius:56px;transform:rotate(45deg);box-shadow:var(--shadow);border:6px solid rgba(255,255,255,.35)}
.tile-label{left:150px;top:712px;width:200px;text-align:center;font-family:'Montserrat',sans-serif;font-weight:700;font-size:15px;line-height:24px;color:var(--white)}
.section-title{font-family:'Montserrat',sans-serif;font-weight:700;font-size:28px}
.body-copy{font-size:14px;line-height:28px;color:var(--white)}
.photo{border-radius:44px;box-shadow:var(--shadow)}
.photo-back{border-radius:44px;background:rgba(255,255,255,.35)}
.products-title{left:0;top:1532px;width:1200px;text-align:center;color:var(--navy)}
.card{width:224px;height:180px;background:var(--white);box-shadow:var(--shadow);display:flex;align-items:center;justify-content:center}
.card-photo{width:150px;height:130px;border-radius:6px}
.card-name{width:236px;text-align:center;font-family:'Montserrat',sans-serif;font-weight:700;font-size:12.5px;line-height:28px}
.price{width:236px;text-align:center;font-family:'Montserrat',sans-serif;font-weight:700;font-size:21px;color:var(--red)}
.service{width:220px;text-align:center}
.service .ring{width:116px;height:116px;border:3px solid var(--navy);border-radius:50%;margin:0 auto;display:flex;align-items:center;justify-content:center}
.service h3{font-family:'Montserrat',sans-serif;font-weight:700;font-size:17px;color:var(--navy);margin-top:30px}
.service p{font-size:14px;line-height:19px;margin-top:20px;padding:0 22px}
.arrow{width:38px;height:38px;border-radius:50%;background:#6c6c6c;display:flex;align-items:center;justify-content:center}
.footer{left:0;top:3270px;width:1200px;height:464px}
.foot-h{font-family:'Montserrat',sans-serif;font-weight:700;font-size:17px;color:var(--white)}
.foot-txt{font-family:'Montserrat',sans-serif;font-size:13px;line-height:20px;color:var(--white)}
.contact-icon{width:46px;height:46px;border:2px solid var(--white);border-radius:50%;display:flex;align-items:center;justify-content:center}
.links{list-style:none}
.links li{font-family:'Montserrat',sans-serif;font-size:14px;line-height:31px;color:var(--white)}
.social{width:44px;height:44px;border:2px solid var(--white);border-radius:50%}
</style>
</head>
<body>
<div class="page">

  <header class="header abs">
    <div class="brand abs">Brackenfield Goods</div>
    <div class="login abs">
      <svg width="24" height="26" viewBox="0 0 24 26"><circle cx="12" cy="7" r="6" fill="#1f4a94"/><path d="M1 26c0-7 5-11 11-11s11 4 11 11z" fill="#1f4a94"/></svg>
      <span>Login/Register</span>
      <svg width="30" height="28" viewBox="0 0 30 28"><path d="M1 3h5l4 15h14l3-11H8" fill="none" stroke="#1f4a94" stroke-width="3"/><circle cx="12" cy="24" r="2.5" fill="#1f4a94"/><circle cx="22" cy="24" r="2.5" fill="#1f4a94"/><circle cx="25" cy="4" r="4" fill="#1f4a94"/></svg>
    </div>
    <nav class="nav abs"><a class="active">Home</a><a>About</a><a>Services</a><a>Products</a><a>Contact us</a></nav>
    <div class="search abs">Search
      <svg class="abs" style="right:10px;top:6px" width="14" height="14" viewBox="0 0 14 14"><circle cx="6" cy="6" r="4.5" fill="none" stroke="#111" stroke-width="1.8"/><path d="M9.5 9.5l3.5 3.5" stroke="#111" stroke-width="1.8"/></svg>
    </div>
  </header>

  <div class="hero abs" role="img" aria-label="Polished steel pipework and valves in a pump room"></div>
  <h1 class="hero-title abs">Welcome to<br>Brackenfield Goods</h1>
  <a class="btn btn-navy abs">Learn More</a>
  <svg class="abs" style="left:40px;top:372px" width="16" height="24" viewBox="0 0 16 24"><path d="M12 3L4 12l8 9" fill="none" stroke="#fff" stroke-width="3"/></svg>
  <svg class="abs" style="left:1144px;top:372px" width="16" height="24" viewBox="0 0 16 24"><path d="M4 3l8 9-8 9" fill="none" stroke="#fff" stroke-width="3"/></svg>

  <div class="blue-a abs"></div>
  <div class="tile abs" style="left:135px;top:624px;background:linear-gradient(135deg,#4d6e98,#24406a)" role="img" aria-label="Worker fitting a large blue valve flange"></div>
  <div class="tile abs" style="left:484px;top:624px;background:linear-gradient(135deg,#5aa6a0,#3b4f7c)" role="img" aria-label="Colour-coded pipes in a plant room"></div>
  <div class="tile abs" style="left:833px;top:624px;background:linear-gradient(135deg,#b59a5a,#3a4f7a)" role="img" aria-label="Brass valves with a red handwheel"></div>
  <div class="tile-label abs">CONSTRUCTION<br>DEWATERING</div>

  <h2 class="section-title abs" style="left:110px;top:990px;color:#fff">ABOUT US</h2>
  <p class="body-copy abs" style="left:110px;top:1036px;width:440px">Lorem Ipsum is simply dummy text of the printing and typesetting industry. Lorem Ipsum has been the industry's standard dummy text ever since the 1500s, when an unknown printer took a galley of type and scrambled it to make a type specimen book. It has survived not only five centuries, but also the leap into electronic typesetting, remaining essentially unchanged</p>
  <a class="btn btn-white abs" style="left:110px;top:1245px">Learn More</a>
  <div class="photo-back abs" style="left:630px;top:952px;width:480px;height:420px;transform:rotate(-4deg)"></div>
  <div class="photo abs" style="left:655px;top:975px;width:440px;height:370px;background:linear-gradient(135deg,#9db6d6,#2c4a78 60%,#16294a)" role="img" aria-label="Industrial pipe gallery in blue tones"></div>

  <svg class="abs" style="left:0;top:1410px" width="1200" height="100" viewBox="0 0 1200 100"><path d="M0 85 Q600 -45 1200 85 L1200 100 L0 100z" fill="#fff"/></svg>

  <h2 class="section-title products-title abs">PRODUCTS</h2>
  <div class="card abs" style="left:107px;top:1636px"><div class="card-photo" style="background:radial-gradient(circle,#f3d65a 0%,#faf3d2 60%,#fff 100%)" role="img" aria-label="Yellow wellpoint swing fitting"></div></div>
  <div class="card abs" style="left:361px;top:1636px"><div class="card-photo" style="background:radial-gradient(circle,#6d5a50 0%,#d9d3cf 60%,#fff 100%)" role="img" aria-label="Dark rubber grommet"></div></div>
  <div class="card abs" style="left:617px;top:1636px"><div class="card-photo" style="background:linear-gradient(160deg,#fff 10%,#d6e6dc 50%,#a9c7e2 80%,#fff)" role="img" aria-label="Blue-tipped wellpoint"></div></div>
  <div class="card abs" style="left:879px;top:1636px"><div class="card-photo" style="background:radial-gradient(circle,#efe6e6 0%,#f6f2f2 55%,#fff 100%)" role="img" aria-label="White PVC ball valve with red handle"></div></div>
  <div class="card-name abs" style="left:101px;top:1830px">STANDARD SWING w/ BALL VALVE - WELLPOINT - DEWATERING - WELL POINT</div>
  <div class="card-name abs" style="left:355px;top:1830px">UNIVERSAL RUBBER GROMMET - DEWATERING - WELLPOINT - WELL POINT - PVC HEADER</div>
  <div class="card-name abs" style="left:611px;top:1830px">HARLOW MFG - WELLPOINT BLUE POINT - 1-1/2" X 3' - STANDARD - DEWATERING</div>
  <div class="card-name abs" style="left:873px;top:1830px">1-1/4" (inch) PVC Ball Valve, Inline, Socket, Slip x Slip Schedule 40</div>
  <div class="price abs" style="left:101px;top:1944px">$1,950.00</div>
  <div class="price abs" style="left:355px;top:1944px">$3.10</div>
  <div class="price abs" style="left:611px;top:1944px">$17.00</div>
  <div class="price abs" style="left:873px;top:1944px">$5.59</div>

  <svg class="abs" style="left:0;top:2060px" width="1200" height="740" viewBox="0 0 1200 740"><path d="M0 10 Q600 180 1200 10 L1200 725 Q600 630 0 725z" fill="#1f4a94"/></svg>
  <div class="photo-back abs" style="left:100px;top:2285px;width:470px;height:420px;transform:rotate(-4deg)"></div>
  <div class="photo abs" style="left:122px;top:2305px;width:440px;height:380px;background:linear-gradient(160deg,#e8e3d6,#8aa3c8 45%,#2b4f9a 75%,#bcbab2)" role="img" aria-label="Row of blue dewatering pumps on a steel skid"></div>
  <h2 class="section-title abs" style="left:640px;top:2330px;color:#fff">DEWATERING PUMPS</h2>
  <p class="body-copy abs" style="left:640px;top:2376px;width:440px">Lorem Ipsum is simply dummy text of the printing and typesetting industry. Lorem Ipsum has been the industry's standard dummy text ever since the 1500s, when an unknown printer took a galley of type and scrambled it to make a type specimen book. It has survived not only five centuries, but also the leap into electronic typesetting, remaining essentially unchanged</p>
  <a class="btn btn-white abs" style="left:640px;top:2580px">Learn More</a>

  <div class="arrow abs" style="left:31px;top:3000px"><svg width="12" height="16" viewBox="0 0 12 16"><path d="M9 2L3 8l6 6" fill="none" stroke="#fff" stroke-width="2.5"/></svg></div>
  <div class="arrow abs" style="left:1131px;top:3000px"><svg width="12" height="16" viewBox="0 0 12 16"><path d="M3 2l6 6-6 6" fill="none" stroke="#fff" stroke-width="2.5"/></svg></div>

  <div class="service abs" style="left:110px;top:2912px">
    <div class="ring"><svg width="60" height="60" viewBox="0 0 60 60" fill="none" stroke="#1f4a94" stroke-width="2.5"><path d="M8 12h30v14H22v8"/><path d="M38 16h10v6H38"/><path d="M22 40c-4 6-4 10 0 10s4-4 0-10z"/></svg></div>
    <h3>PUMPS</h3><p>Lorem Ipsum is simply dummy text of the printing and typesetting industry. Lorem Ipsum has been the industry's</p>
  </div>
  <div class="service abs" style="left:360px;top:2912px">
    <div class="ring"><svg width="60" height="60" viewBox="0 0 60 60" fill="none" stroke="#1f4a94" stroke-width="2.5"><path d="M6 52V30l12-8v8l12-8v8l12-8V10h8v42z"/><rect x="14" y="40" width="6" height="6"/><rect x="28" y="40" width="6" height="6"/></svg></div>
    <h3>MANUFACTURING</h3><p>Lorem Ipsum is simply dummy text of the printing and typesetting industry. Lorem Ipsum has been the industry's</p>
  </div>
  <div class="service abs" style="left:620px;top:2912px">
    <div class="ring"><svg width="64" height="64" viewBox="0 0 64 64"><circle cx="32" cy="28" r="12" fill="none" stroke="#1f4a94" stroke-width="8" stroke-dasharray="6 3"/><circle cx="32" cy="28" r="5" fill="#1f4a94"/><path d="M8 52h48" stroke="#1f4a94" stroke-width="3"/></svg></div>
    <h3>INSTALLATIONS</h3><p>Lorem Ipsum is simply dummy text of the printing and typesetting industry. Lorem Ipsum has been the industry's</p>
  </div>
  <div class="service abs" style="left:880px;top:2912px">
    <div class="ring"><svg width="60" height="60" viewBox="0 0 60 60" fill="none" stroke="#1f4a94" stroke-width="2.5"><rect x="8" y="8" width="44" height="32"/><path d="M18 34V24M26 34V18M34 34V22M42 34V14"/><path d="M30 40v6M20 54l10-8 10 8"/></svg></div>
    <h3>PROJECTS</h3><p>Lorem Ipsum is simply dummy text of the printing and typesetting industry. Lorem Ipsum has been the industry's</p>
  </div>

  <svg class="footer abs" width="1200" height="464" viewBox="0 0 1200 464"><path d="M0 30 Q600 -10 1200 30 L1200 464 L0 464z" fill="#1f4a94"/></svg>
  <div class="foot-h abs" style="left:172px;top:3366px">CONTACT US</div>
  <div class="contact-icon abs" style="left:172px;top:3418px"><svg width="20" height="26" viewBox="0 0 20 26"><path d="M10 25S2 15 2 9a8 8 0 0116 0c0 6-8 16-8 16z" fill="none" stroke="#fff" stroke-width="2.5"/><circle cx="10" cy="9" r="3" fill="#fff"/></svg></div>
  <div class="foot-txt abs" style="left:232px;top:3418px">2240 Marlow Creek Road<br>Tessaly</div>
  <div class="contact-icon abs" style="left:172px;top:3490px"><svg width="22" height="22" viewBox="0 0 22 22"><path d="M4 2l4 1 2 5-3 2c1 3 3 5 6 6l2-3 5 2 1 4c-1 2-3 2-5 2C8 21 1 14 1 6c0-2 1-4 3-4z" fill="#fff"/></svg></div>
  <div class="foot-txt abs" style="left:232px;top:3503px">1 800 555 0142</div>
  <div class="contact-icon abs" style="left:172px;top:3563px"><svg width="24" height="18" viewBox="0 0 24 18"><rect x="1" y="1" width="22" height="16" fill="#fff"/><path d="M1 1l11 9 11-9" fill="none" stroke="#1f4a94" stroke-width="2"/></svg></div>
  <div class="foot-txt abs" style="left:232px;top:3576px">info@brackenfieldgoods.com</div>
  <div class="foot-txt abs" style="left:172px;top:3650px">Copyright © 2018. All rights reserved</div>

  <div class="foot-h abs" style="left:545px;top:3366px">QUICK LINK</div>
  <ul class="links abs" style="left:545px;top:3406px"><li>Home</li><li>About Us</li><li>Services</li><li>Products</li><li>Contact us</li></ul>

  <div class="foot-h abs" style="left:790px;top:3366px">FOLLOW US ON</div>
  <div class="abs" style="left:790px;top:3418px;width:282px;height:178px;background:linear-gradient(135deg,#e4e6e2,#cfd6cc)" role="img" aria-label="Street map showing the store location"></div>
  <div class="social abs" style="left:790px;top:3605px"></div>
  <div class="social abs" style="left:848px;top:3605px"></div>
  <div class="social abs" style="left:906px;top:3605px"></div>

</div>
</body>
</html>
```